K&R Security Services PTY. LTD.

Ive just had my logo made and I'm looking for some simple but strong designs for my business cards the company is a security company.

Please use dark colors.

Regards,

Owen Deloit

Reason: Need more time for discussion with other directors

Industry/Entity Type

Security

Font styles to use
Sans Serif
Decorative

```html
<!DOCTYPE html>
<html lang="en">
<head>
<meta charset="utf-8">
<title>K&amp;R Security Services – Business Card</title>
<link href="https://fonts.googleapis.com/css2?family=Open+Sans:wght@400;600;700&display=swap" rel="stylesheet">
<style>
  :root {
    --backdrop: #3a3835;
    --card: #dcdcdc;
    --ink: #2a2a2a;
    --ink-soft: #4a4a4a;
    --icon-bg: #5a5a5a;
    --icon-fg: #ffffff;
  }
  * { margin: 0; padding: 0; box-sizing: border-box; }
  html, body { width: 1200px; height: 897px; overflow: hidden; }
  body {
    background: var(--backdrop);
    font-family: "Open Sans", Arial, sans-serif;
    color: var(--ink);
    position: relative;
  }
  .card {
    position: absolute;
    background: var(--card);
    border-radius: 34px;
    box-shadow: 0 10px 28px rgba(0,0,0,0.35);
  }
  .card-back { left: 140px; top: 288px; width: 560px; height: 320px; }
  .card-front { left: 740px; top: 168px; width: 320px; height: 560px;
    display: flex; align-items: center; justify-content: center; }

  .contact-list {
    position: absolute; right: 34px; top: 34px;
    list-style: none; display: flex; flex-direction: column; gap: 14px;
  }
  .contact-item {
    display: flex; align-items: center; justify-content: flex-end; gap: 12px;
    font-size: 11px; line-height: 1.35; text-transform: uppercase;
    color: var(--ink-soft); text-align: right; letter-spacing: 0.2px;
  }
  .contact-icon {
    width: 26px; height: 26px; border-radius: 5px; background: var(--icon-bg);
    display: flex; align-items: center; justify-content: center; flex: none;
  }
  .contact-icon svg { width: 15px; height: 15px; }

  .identity { position: absolute; left: 38px; bottom: 40px; }
  .identity-name { font-size: 19px; text-transform: uppercase; color: var(--ink); letter-spacing: 0.3px; }
  .identity-name .first { font-weight: 700; }
  .identity-name .last { font-weight: 400; }
  .identity-role { font-size: 11px; text-transform: uppercase; color: var(--ink-soft); margin-top: 2px; }

  .brand-name {
    font-weight: 700; font-size: 30px; line-height: 1.15; text-align: center;
    color: var(--ink); text-transform: uppercase;
  }
  .brand-name small { display: block; font-size: 14px; letter-spacing: 1.5px; margin-top: 6px; font-weight: 700; }
</style>
</head>
<body>

<section class="card card-back">
  <ul class="contact-list">
    <li class="contact-item">
      <span>012 555 0147<br>012 555 0148</span>
      <span class="contact-icon"><svg viewBox="0 0 16 16"><path fill="var(--icon-fg)" d="M4 1.5l2.2 3-1.3 1.5c.8 1.8 2.3 3.3 4.1 4.1L10.5 8.8l3 2.2-1 2.6C7.1 13.6 2.4 8.9 1.4 2.5z"/></svg></span>
    </li>
    <li class="contact-item">
      <span>www.krsecurity.example<br>krsecurity.example</span>
      <span class="contact-icon"><svg viewBox="0 0 16 16" fill="none" stroke="var(--icon-fg)" stroke-width="1.3"><circle cx="8" cy="8" r="6.2"/><ellipse cx="8" cy="8" rx="2.6" ry="6.2"/><path d="M1.8 8h12.4M3 4.6h10M3 11.4h10"/></svg></span>
    </li>
    <li class="contact-item">
      <span>contact@krsecurity.example<br>info@krsecurity.example</span>
      <span class="contact-icon"><svg viewBox="0 0 16 16" fill="none" stroke="var(--icon-fg)" stroke-width="1.3"><rect x="2" y="3.5" width="12" height="9" rx="1"/><path d="M2.3 4l5.7 4.6L13.7 4"/></svg></span>
    </li>
    <li class="contact-item">
      <span>48 Harbour Lane, Northgate 9710<br>United Kingdom</span>
      <span class="contact-icon"><svg viewBox="0 0 16 16"><path fill="var(--icon-fg)" d="M8 1a4.6 4.6 0 0 0-4.6 4.6C3.4 9.2 8 15 8 15s4.6-5.8 4.6-9.4A4.6 4.6 0 0 0 8 1zm0 6.5a1.9 1.9 0 1 1 0-3.8 1.9 1.9 0 0 1 0 3.8z"/></svg></span>
    </li>
  </ul>

  <div class="identity">
    <p class="identity-name"><span class="first">Owen</span> <span class="last">Deloit</span></p>
    <p class="identity-role">Senior Graphic Designer</p>
  </div>
</section>

<section class="card card-front">
  <p class="brand-name">K&amp;R Security<br>Services<small>PTY. LTD.</small></p>
</section>

</body>
</html>
```